Dentistry Office

We want a new design for a Dentist's office website.

The theme is: "We provide high quality, state-of-the-art, dental care in a comfortable, caring environment."

The site currently has a menu on the left of the page with about 40 items on it. There is a great deal of textual content on each page, plus several illustrations.

We want to do this using CSS, so we need specifications in the CSS for all possible elements. The CSS needs to be named in a logical manner for easy use.

Every dentist on the planet seems to use lots of Flash. We don't want to because it is so distracting. We are looking for an elegant solution targeting 24-55 age group, but not excluding anyone.

The following (from another dentist's site) can give you a taste of what we want to communicate on the site:

"After 20 years of teaching dentists how to refine their technique and many years of writing textbooks, I currently devote my time to my office and the hands-on practice of dentistry. I'd like to welcome you personally to my dental practice, and I invite you to meet my highly experienced team of professionals.

"We have offered complete dental care of the highest quality since 1978. We provide Preventive Services, Tooth Whitening and Cosmetic Dentistry for a beautiful smile, Endodontics (root canal treatment) to treat painful teeth, Sedation Dentistry so you can relax, and Dental Implants to restore what is missing. We offer total care.

"Our approach to your health is simple: We use our education, experience and dedication to provide every patient with superior dental care.

"This passion for excellence is not just a goal, but a standard every member of our team holds.

"We also pride ourselves with our state of the art procedures, training and technology. This includes creating a beautiful smile using techniques that preserve as much of the original tooth as possible.

"Our abilities are renowned throughout the dental profession and I hope if you have any questions you will contact us by an e-mail note, by phone or just by dropping by."

Keep in mind the screen shape and dimensions. Your design needs to work in the normal screen proportions, regardless of how it looks when you post it here. Scrolling is OK, but the first impression needs to work.

Keep in mind that there will be about 250 words, or more, on each page.

Competitors web sites:

http://www.brevalkoortho.example/

http://www.quimbelfieldcare.example/

http://www.grinsatdoverellclinic.example/

http://www.trunwickfamilydentalcare.example/

http://www.morvanhaledental.example/

http://www.ubrigandental.example/

We need to compete with these.

Target Market(s)

Generally adults seeking the most experienced and comfortable-to-be-with dentist.

Industry/Entity Type

Training

Requirements
Must have
• Must stand apart from other dentists.
• Must be elegant.
• Must have a horizontal menu structure across all columns, NOT a vertical that requires scrolling, no popout, pop down, etc. menus.
• We are looking for something special.
• Do not waste your time or ours putting up templates and things you have used before.
• Personally, I do not see how someone outside the US can understand the northern California dental market. But you are welcome to try.
Should not have
• Flash or graphics that move
• The look of a template
• Folksy fonts
• Looks like you used it 20 times before

```html
<!DOCTYPE html>
<html lang="en">
<head>
<meta charset="utf-8">
<title>Larkvale Dentist – Home</title>
<link rel="stylesheet" href="https://fonts.googleapis.com/css2?family=Arimo:wght@400;700&family=Roboto+Condensed:wght@400&display=swap">
<style>
:root{
  --brand:#2b6688;
  --brand-dark:#1f4f6b;
  --ink:#4a4a4a;
  --ink-soft:#666;
  --heading:#555;
  --rule:#c9d2d8;
  --panel:#ffffff;
  --tab:#d5dee4;
  --stage:#eef0f2;
  --footer-top:#e4e5e7;
  --footer-bottom:#f6f6f7;
}
*{box-sizing:border-box;margin:0;padding:0}
html,body{width:1200px;height:900px;overflow:hidden}
body{background:var(--stage);font-family:"Arimo",Arial,sans-serif;color:var(--ink);position:relative}
a{color:inherit;text-decoration:none}
ul{list-style:none}

.page{position:absolute;left:88px;top:0;width:1026px;height:900px;background:linear-gradient(#ffffff 0,#ffffff 60px,#e9eaec 178px,#f3f3f4 240px,#f7f7f8 760px);border-left:1px solid #cfd2d5;border-right:1px solid #cfd2d5}

/* header */
.brand{position:absolute;left:62px;top:84px;display:flex;align-items:center;gap:10px}
.brand-mark{width:62px;height:60px;border-radius:10px;background:var(--brand)}
.brand-name{font-family:"Roboto Condensed","Arial Narrow",sans-serif;font-size:33px;line-height:36px;margin-top:-22px;color:var(--brand);font-weight:400;letter-spacing:-.2px}
.utility-nav{position:absolute;left:798px;top:89px;display:flex;gap:22px;font-size:12px;color:#333}
.utility-nav a::before,.crumbs li::before{content:"";display:inline-block;border-left:5px solid var(--brand);border-top:3px solid transparent;border-bottom:3px solid transparent;margin-right:4px;vertical-align:1px}
.search{position:absolute;left:798px;top:128px;width:182px;height:19px;border:1px solid #b9bcc0;background:#fff;font-size:12px;color:#999;padding:2px 8px}
.search svg{position:absolute;right:6px;top:3px}

/* main navigation */
.main-nav{position:absolute;left:0;top:178px;width:1026px;height:27px;background:linear-gradient(#3a7596,var(--brand) 50%,var(--brand-dark));border:1px solid #a9c0cf;box-shadow:inset 0 0 0 1px #5f8ea9;display:flex;padding-left:63px}
.main-nav a{color:#fff;font-size:15.5px;line-height:25px;padding:0 17px}
.main-nav a.is-current{background:#7b7f83;padding:0 9px;margin-right:9px}

/* sidebar */
.sidebar{position:absolute;left:785px;top:205px;width:203px;height:525px;background:var(--panel);box-shadow:0 2px 6px rgba(0,0,0,.25)}
.page-tools{position:absolute;left:14px;top:80px;font-size:12px;color:#333}
.page-tools li{display:flex;align-items:center;gap:10px;height:22px}
.section-tab{position:absolute;left:1px;width:201px;height:21px;background:linear-gradient(#e8edf1,var(--tab));border:1px solid #a6bccb;color:var(--brand);font-size:13.5px;line-height:19px;padding-left:28px}
.section-tab::before{content:"";position:absolute;left:12px;top:7px;border-left:5px solid #fff;border-top:3px solid transparent;border-bottom:3px solid transparent}
.section-tab.is-open::before{left:11px;top:7px;border-top:5px solid #fff;border-left:4px solid transparent;border-right:4px solid transparent;border-bottom:0}
.sub-links{position:absolute;left:16px;top:197px;font-size:12px;color:#444}
.sub-links li{display:flex;align-items:center;gap:9px;height:22px}
.sub-links li::before{content:"";width:11px;height:11px;border-radius:50%;background:radial-gradient(circle at 55% 50%,#fff 0 2px,var(--brand) 2.5px)}
.emergency{position:absolute;left:16px;top:443px;display:flex;gap:10px}
.emergency-label{font-size:18px;font-weight:700;letter-spacing:2px;color:var(--brand)}
.emergency-phone{font-size:16px;font-weight:700;color:#333;margin-top:10px}

/* content */
.crumbs{position:absolute;left:84px;top:251px;display:flex;gap:14px;font-size:10px;color:#777}
.crumbs li::before{border-left-color:#888}
.crumbs li.is-current{color:var(--brand)}
.crumbs li.is-current::before{border-left-color:var(--brand)}
.page-title{position:absolute;left:78px;top:286px;width:700px;font-weight:400;font-size:22px;line-height:26px;color:var(--heading);white-space:nowrap}
.lead{position:absolute;left:78px;top:354px;width:656px;font-size:16.5px;color:var(--brand);letter-spacing:.1px;white-space:nowrap}
.lead-line{display:block;height:30px;line-height:29px;padding-left:2px;border-bottom:1px solid var(--rule)}
.lead-line.is-last{display:inline-block;padding-right:4px}
.col{position:absolute;top:462px;font-size:12px;line-height:22px;color:var(--ink-soft)}
.col-intro{left:80px;width:346px}
.col-approach{left:444px;width:300px}
.portrait{float:left;width:118px;height:100px;margin:4px 28px 28px 4px;border-radius:6px;background:linear-gradient(135deg,#b75a5a,#e8c3b6 45%,#f3eee8 60%,#9e3b3e);box-shadow:0 0 0 4px #fff,0 2px 6px 4px rgba(0,0,0,.18)}

/* footer */
.site-footer{position:absolute;left:0;top:772px;width:1024px;height:128px;background:linear-gradient(var(--footer-top),var(--footer-bottom))}
.footer-col{position:absolute;font-size:12px;line-height:18px;color:#555}
.footer-col h3{font-size:14px;font-weight:700;color:var(--brand);margin-bottom:6px}
.footer-col li{display:flex;align-items:center;gap:9px}
.footer-col li::before{content:"";width:11px;height:11px;border-radius:50%;background:radial-gradient(circle at 55% 50%,#fff 0 2px,#555 2.5px)}
.footer-contact b{color:var(--brand)}
.footer-contact a{color:var(--brand)}
</style>
</head>
<body>
<div class="page">
  <header>
    <a class="brand" href="#"><span class="brand-mark"></span><span class="brand-name">Larkvale Dentist</span></a>
    <nav class="utility-nav"><a href="#">home</a><a href="#">sitemap</a><a href="#">contact</a></nav>
    <div class="search">search...
      <svg width="12" height="12" viewBox="0 0 12 12"><circle cx="5" cy="5" r="3.8" fill="none" stroke="#999" stroke-width="1.5"/><line x1="8" y1="8" x2="11.5" y2="11.5" stroke="#999" stroke-width="1.8"/></svg>
    </div>
  </header>

  <nav class="main-nav">
    <a class="is-current" href="#">Home Page</a>
    <a href="#">Why we are different</a>
    <a href="#">Technologies we offer</a>
    <a href="#">Meet Dr. Keswick</a>
    <a href="#">Our Staff</a>
    <a href="#">Contact Us</a>
  </nav>

  <ul class="crumbs"><li>home</li><li>parent page</li><li class="is-current">current page</li></ul>

  <h1 class="page-title">Providing Cosmetic Dentistry Excellence to Patients in<br>Larkvale, Brenmoor County and the Northern Harbor Area</h1>
  <p class="lead">
    <span class="lead-line">In Larkvale, when you’re a patient of Dr. Keswick, you can be confident that you’re re-</span>
    <span class="lead-line">ceiving care from the most experienced, knowledgeable, and skilled cosmetic dentist in</span>
    <span class="lead-line is-last">Brenmoor County.</span>
  </p>

  <div class="col col-intro">
    <div class="portrait" role="img" aria-label="Photo of a smile with a clear dental aligner"></div>
    <p>Dr. Keswick is an award-winning leader in restorative dentistry and a genial professional. His humor, dedication, and talent ensure you a pleasant experience and superb, long-lasting results.</p>
    <p>After 25 years of teaching dentists how to refine their technique and many years of writing textbooks, I currently devote my time to my office and the hands-on practice of dentistry. I'd like to welcome you personally to my dental practice, and I invite you to meet my highly experienced team of professionals.</p>
    <p>Lorem vestibulum in massa ac ipsum pharetra faucibus.</p>
  </div>

  <div class="col col-approach">
    <p>Our approach to your health is simple: We use our education, experience and dedication to provide every patient with superior dental care.</p>
    <p>This passion for excellence is not just a goal, but a standard every member of our team holds.</p>
    <p>We also pride ourselves with our state of the art proce­dures, training and technology. This includes creating a beautiful smile using techniques that preserve as much of the original tooth as possible. Our abilities are renowned throughout the dental profession and I hope if you have any questions you will contact us by an e-mail note, by phone or just by dropping by.</p>
  </div>

  <aside class="sidebar">
    <ul class="page-tools">
      <li><svg width="15" height="13" viewBox="0 0 15 13"><rect x="4" y="0" width="7" height="4" fill="#444"/><rect x="0" y="4" width="15" height="6" rx="1" fill="#444"/><rect x="3.5" y="8" width="8" height="5" fill="#fff" stroke="#444"/></svg>print this page</li>
      <li><svg width="15" height="11" viewBox="0 0 15 11"><rect width="15" height="11" fill="#444"/><path d="M0 0 7.5 6 15 0M0 11 6 5M15 11 9 5" stroke="#fff" fill="none"/></svg>e-mail this page</li>
    </ul>
    <div class="section-tab is-open" style="top:160px">Education</div>
    <ul class="sub-links">
      <li>Emergency Dental Care</li>
      <li>Your Mouth</li>
      <li>Your Tooth</li>
      <li>Cracked Tooth?</li>
    </ul>
    <div class="section-tab" style="top:296px">Preventative</div>
    <div class="section-tab" style="top:318px">Education</div>
    <div class="section-tab" style="top:340px">Cosmetics</div>
    <div class="section-tab" style="top:362px">Restorations</div>
    <div class="section-tab" style="top:384px">Visiting our office</div>
    <div class="emergency">
      <svg width="22" height="52" viewBox="0 0 22 52"><path d="M9 2c-7 3-9 14-7 26 2 11 8 20 16 22l3-8-6-4-4 3c-3-6-4-14-3-20l5-1 1-8z" fill="var(--brand)"/></svg>
      <div><div class="emergency-label">Emergency</div><div class="emergency-phone">(555) 418-2063</div></div>
    </div>
  </aside>

  <footer class="site-footer">
    <div class="footer-col" style="left:82px;top:32px">
      <h3>About Harold Keswick</h3>
      <ul><li>lorem ipsum dolar sit</li><li>lorem ipsum dolar sit</li><li>lorem ipsum dolar sit</li></ul>
    </div>
    <div class="footer-col" style="left:324px;top:26px">
      <h3>Technologies we offer</h3>
      <ul><li>lorem ipsum dolar sit</li><li>lorem ipsum dolar sit</li><li>lorem ipsum dolar sit</li></ul>
    </div>
    <div class="footer-col" style="left:562px;top:26px">
      <h3>Address</h3>
      <p>48 Orchard Avenue<br>Larkvale</p>
    </div>
    <div class="footer-col footer-contact" style="left:798px;top:38px">
      <p><b>T</b> (555) 730-4417<br><b>F</b> 0411 286 305<br><a href="#">drkeswick@larkvaledental.example</a></p>
    </div>
  </footer>
</div>
</body>
</html>
```